Summer Music/Chorus/Choir Camp for Young Singers Ages 8-13

We need a flyer for a summer camp for young singers ages 8-13. We are nonprofit community children's chorus in Miami, FL. Our camp provides specialized training in music theory, sight-reading,and aural training through daily choral rehearsals in an environment that is both positive and a lot of fun! Our camp offers children the opportunity to come as they are, no matter the level of experience, and grow tremendously in their musicianship skills. In addition to this, our campers participate in song-writing, masterclasses, community performances, and media projects. The final design should be clean, fun, not too crowded, should appeal to boys and girls ages 8-13, and something someone that age would consider "cool" and not too childish. Drawings are cool, something different.
Updates

Target Market(s)

Ages 8-13 and parents of those kids.

Industry/Entity Type

Community

Requirements
Must have
• All info attached.
Nice to have
• Things that relate to music, especially related to singing/choirs
Should not have
• instruments, stock photos of children, or photos from our website (unless they are used very creatively), or photos in general. I've attached our previous camp flyer and our current organization flyer but I don't necessarily want this flyer to look like those.

```html
<!DOCTYPE html>
<html lang="en">
<head>
<meta charset="utf-8">
<title>Summer Music Camp</title>
<link href="https://fonts.googleapis.com/css2?family=Anton&family=Alfa+Slab+One&family=Lato:wght@400;700;900&family=Oswald:wght@300;400&display=swap" rel="stylesheet">
<style>
  :root{
    --yellow:#f7e21c;
    --yellow-light:#fff45a;
    --pink:#e5127d;
    --blue:#1b5fc4;
    --green:#2e9a1e;
    --stripe-green:#22a12a;
    --white:#ffffff;
    --ink:#1a1a1a;
    --wood-top:#7b2a12;
    --wood-bottom:#230a05;
    --accent-yellow:#ffe51a;
  }
  *{margin:0;padding:0;box-sizing:border-box}
  html,body{width:900px;height:1200px;overflow:hidden;background:#ffffff}
  .flyer{position:relative;width:900px;height:1200px;overflow:hidden;
    background:radial-gradient(circle at 460px 420px,var(--yellow-light) 0%,var(--yellow) 55%,#f2d60f 100%);
    font-family:'Lato',sans-serif}
  .layer{position:absolute;left:0;top:0}
  .photo{position:absolute;left:0;top:230px;width:850px;height:530px;
    background:radial-gradient(ellipse at 30% 60%,rgba(120,170,220,.55) 0%,rgba(120,170,220,0) 45%),
               radial-gradient(ellipse at 70% 45%,rgba(230,110,80,.5) 0%,rgba(230,110,80,0) 55%);}
  .footer{position:absolute;left:0;top:760px;width:900px;height:440px;
    background:linear-gradient(180deg,var(--wood-top) 0%,#4b170a 60%,var(--wood-bottom) 100%)}
  .footer-band{position:absolute;left:0;top:1183px;width:900px;height:17px;background:var(--stripe-green)}
  .title-summer{position:absolute;left:46px;top:30px;font-family:'Anton',sans-serif;font-weight:400;font-size:150px;
    line-height:1;color:var(--pink);letter-spacing:1px}
  .title-camp{position:absolute;left:50px;top:178px;font-family:'Alfa Slab One',serif;font-size:64px;line-height:1;letter-spacing:1px;white-space:nowrap}
  .title-camp .music{color:var(--blue)}
  .title-camp .camp{color:var(--green)}
  .price{position:absolute;left:662px;top:66px;width:226px;text-align:center}
  .price-amount{font-weight:900;font-size:50px;color:var(--green);line-height:1}
  .price-note{font-weight:700;font-size:25px;color:var(--ink);margin-top:8px;white-space:nowrap}
  .age-badge{position:absolute;left:49px;top:551px;width:248px;height:248px;border-radius:50%;
    background:var(--pink);border:15px solid var(--blue);text-align:center;color:var(--white);
    font-family:'Anton',sans-serif;display:flex;flex-direction:column;justify-content:center;line-height:1}
  .age-badge .for{font-size:46px}
  .age-badge .range{font-size:80px;color:var(--accent-yellow)}
  .age-badge .years{font-size:44px}
  .description{position:absolute;left:345px;top:560px;width:535px;text-align:center}
  .description h2{font-family:'Alfa Slab One',serif;font-weight:400;font-size:32px;color:var(--pink);letter-spacing:1px;white-space:nowrap}
  .description p{font-weight:700;font-size:16px;line-height:21px;color:var(--ink);margin-top:6px}
  .org{position:absolute;left:82px;top:870px;display:flex;align-items:center;gap:14px}
  .org-dot{width:26px;height:26px;border-radius:50%;background:var(--white)}
  .org-name{font-weight:400;font-size:30px;color:var(--white);line-height:1.1}
  .partner-square{position:absolute;left:65px;top:997px;width:46px;height:74px;background:var(--white)}
  .partner-rect{position:absolute;left:172px;top:1018px;width:189px;height:35px;background:var(--white)}
  .contact{position:absolute;left:20px;top:1082px;width:420px;text-align:center}
  .phone{font-weight:900;font-size:32px;line-height:1.1;color:var(--accent-yellow);white-space:nowrap}
  .address{margin-top:6px;font-weight:700;font-size:15px;color:var(--white);line-height:1.3;white-space:nowrap}
  .schedule{position:absolute;left:459px;top:872px;width:420px}
  .date{font-family:'Oswald',sans-serif;font-weight:300;font-size:108px;color:var(--white);line-height:1;white-space:nowrap}
  .hours{margin-top:6px;font-family:'Oswald',sans-serif;font-weight:300;font-size:68px;color:var(--white);line-height:1;white-space:nowrap}
  .extended{margin-top:10px;width:395px;font-weight:900;font-size:20px;color:var(--accent-yellow);line-height:1.3}
  .email{position:absolute;left:462px;top:1144px;font-weight:700;font-size:18px;color:var(--white);white-space:nowrap}
</style>
</head>
<body>
<main class="flyer">
  <svg class="layer" width="900" height="1200" aria-hidden="true">
    <rect x="664" y="0" width="51" height="760" fill="var(--pink)"/>
    <rect x="753" y="0" width="71" height="760" fill="var(--blue)"/>
    <rect x="838" y="0" width="62" height="760" fill="var(--stripe-green)"/>
  </svg>

  <div class="photo" role="img" aria-label="Photo of cheerful children raising their arms, a girl in sunglasses and denim jacket beside a vintage microphone"></div>

  <div class="footer"></div>
  <div class="footer-band"></div>

  <h1 class="title-summer">SUMMER</h1>
  <div class="title-camp"><span class="music">MUSIC</span> <span class="camp">CAMP</span></div>

  <svg class="layer" width="900" height="1200" aria-hidden="true">
    <defs>
      <g id="price-cloud">
        <circle cx="695" cy="100" r="48"/><circle cx="752" cy="58" r="55"/>
        <circle cx="840" cy="52" r="60"/><circle cx="890" cy="115" r="55"/>
        <circle cx="835" cy="160" r="38"/><circle cx="725" cy="155" r="40"/>
        <rect x="690" y="60" width="210" height="115"/>
      </g>
      <g id="desc-cloud">
        <circle cx="345" cy="550" r="68"/><circle cx="480" cy="508" r="78"/>
        <circle cx="640" cy="500" r="80"/><circle cx="795" cy="512" r="74"/>
        <circle cx="885" cy="565" r="60"/><circle cx="870" cy="785" r="50"/>
        <circle cx="730" cy="815" r="55"/><circle cx="570" cy="822" r="55"/>
        <circle cx="410" cy="812" r="55"/><circle cx="295" cy="765" r="58"/>
        <circle cx="265" cy="650" r="58"/>
        <rect x="275" y="540" width="625" height="270"/>
      </g>
    </defs>
    <use href="#price-cloud" fill="var(--pink)" stroke="var(--pink)" stroke-width="12"/>
    <use href="#price-cloud" fill="var(--white)"/>
    <use href="#desc-cloud" fill="var(--yellow)" stroke="var(--yellow)" stroke-width="26"/>
    <use href="#desc-cloud" fill="var(--pink)" stroke="var(--pink)" stroke-width="12"/>
    <use href="#desc-cloud" fill="var(--white)"/>
  </svg>

  <div class="price">
    <div class="price-amount">*$300</div>
    <div class="price-note">2-week session</div>
  </div>

  <section class="description">
    <h2>*CAMP DESCRIPTION</h2>
    <p>"Youth and children who love to sing will have a blast at our choral camp! Our music educators and industry professionals are dedicated to enhancing the lives of young singers through choral training which develops vocal technique, ear-training, music reading, and interpersonal skills. Activities are fun and interactive and former music training is not necessary. Singers in grades 3-9 are invited to attend! Register today!"</p>
  </section>

  <div class="age-badge">
    <span class="for">FOR</span>
    <span class="range">8-13</span>
    <span class="years">YEARS</span>
  </div>

  <div class="org">
    <span class="org-dot"></span>
    <span class="org-name">Bright Harmony<br>Youth Chorus</span>
  </div>
  <div class="partner-square"></div>
  <div class="partner-rect"></div>

  <div class="contact">
    <div class="phone">Phone- 305.555.0148</div>
    <div class="address">Coral Bay Community Arts Center,<br>4200 SW Palm Grove Avenue Miami, FL 33190</div>
  </div>

  <div class="schedule">
    <div class="date">July 18-29</div>
    <div class="hours">9am-3pm (M-F)*</div>
    <div class="extended">*Extended hours available (7:30am-5:30pm) for an extra $50 per week.</div>
  </div>
  <div class="email">Email- info@brightharmonychorus.org</div>
</main>
</body>
</html>
```